Poster for a new "Pizza Roll" Combo at our bakery

We are a cinnamon roll and coffee focused bakery, but we would like an innovative poster design to bring attention to our new offering, a Pizza Roll. We will be offering it as a combo, and this is what we wish to advertise. It will be geared mainly towards a younger high school aged crowd. I have included pics of the Pizza Rolls, but it's up to you how you want to incorporate them in the design.Poster should include our logo, the pizza rolls, and can include a drink to illustrate the combo as well. ( we offer710 ml vima bottle products and lurn bottled waters)Main Text: Try our amazing new Pizza Rolls! Message to get accross: $6.00 for a Pizza Roll and drink.Small Print: Avail after 11am, while supplies last. Includes one pizza roll and one bottled drink of choice. Taxes extra.

Target Market(s)

Broad, but mainly high school aged kids

Industry/Entity Type

Bakery

Colors

Designer to choose colors to be used in the design.

Requirements
Must have
• Text: " Try our amazing new PIzza Rolls!:
• $6 Pizza Roll Combo (Pizza Roll and a drink)
Nice to have
• Pic of the PIzza Roll (photo shopped if needed to improve esthetics)
• Pic of a Bottled 710ml vima drink
Should not have
• Any animal product references, as we are a Vegan shop.

```html
<!DOCTYPE html>
<html lang="en">
<head>
<meta charset="UTF-8">
<title>Pizza Roll Combo Poster</title>
<link href="https://fonts.googleapis.com/css2?family=Archivo+Black&family=Fira+Sans:wght@400;500&family=Playball&display=swap" rel="stylesheet">
<style>
  :root {
    --backdrop: #e9e6e1;
    --orange-bright: #f7a23a;
    --orange-mid: #e98a22;
    --orange-deep: #b85e12;
    --grunge-dark: #5a3210;
    --ink: #161311;
    --white: #ffffff;
    --sticker-red: #d9141e;
    --sticker-dark: #9e0c12;
    --band: #1e1c1b;
  }
  * { margin: 0; padding: 0; box-sizing: border-box; }
  html, body {
    width: 1200px;
    height: 1200px;
    overflow: hidden;
    background: var(--backdrop);
  }
  .poster {
    position: absolute;
    left: 260px;
    top: 0;
    width: 680px;
    height: 1200px;
    overflow: hidden;
    background:
      radial-gradient(ellipse at 50% 55%, var(--orange-bright) 0%, var(--orange-mid) 45%, var(--orange-deep) 80%, var(--grunge-dark) 100%);
  }
  .headline-script {
    position: absolute;
    left: 0;
    right: 0;
    top: 95px;
    text-align: center;
    font-family: "Playball", cursive;
    font-weight: 400;
    color: var(--white);
    line-height: 0.9;
    transform: rotate(4deg);
  }
  .headline-script .line-try { display: block; font-size: 78px; padding-left: 110px; }
  .headline-script .line-amazing { display: block; font-size: 96px; padding-left: 30px; }
  .headline-main {
    position: absolute;
    left: 0;
    right: 0;
    top: 300px;
    text-align: center;
    font-family: "Archivo Black", sans-serif;
    font-size: 62px;
    color: var(--ink);
    letter-spacing: 1px;
    transform: rotate(3.5deg);
    white-space: nowrap;
  }
  .combo-illustration {
    position: absolute;
    left: 70px;
    top: 450px;
    width: 560px;
    height: 490px;
    border-radius: 50% 50% 30% 30%;
    background: radial-gradient(ellipse at 40% 65%, #d98a3c 0%, #b8652a 45%, #c43a2c 75%, rgba(196,58,44,0) 100%);
  }
  .price-sticker {
    position: absolute;
    left: 92px;
    top: 395px;
    width: 190px;
    height: 190px;
    border-radius: 50%;
    background: radial-gradient(circle at 40% 35%, var(--sticker-red) 0%, var(--sticker-dark) 100%);
    color: var(--white);
    font-family: "Fira Sans", sans-serif;
    text-align: center;
    padding-top: 22px;
  }
  .price-sticker .price { display: block; font-size: 64px; font-weight: 500; line-height: 1; }
  .price-sticker .label { display: block; font-size: 28px; line-height: 1.1; }
  .small-print {
    position: absolute;
    left: 40px;
    top: 985px;
    width: 600px;
    padding: 18px 20px;
    background: var(--band);
    color: var(--white);
    font-family: "Fira Sans", sans-serif;
    font-size: 20px;
    line-height: 1.35;
    text-align: center;
    transform: rotate(-2.5deg);
  }
</style>
</head>
<body>
  <main class="poster">
    <h1 class="headline-script">
      <span class="line-try">Try our</span>
      <span class="line-amazing">Amazing new</span>
    </h1>
    <div class="headline-main">PIZZA ROLLS!</div>
    <div class="combo-illustration" role="img" aria-label="Illustration of a glazed pizza roll with cinnamon sticks beside a red drink cup with a straw"></div>
    <div class="price-sticker">
      <span class="price">$6</span>
      <span class="label">Pizza Roll<br>Combo</span>
    </div>
    <p class="small-print">Avail after 11am, while supplies last. Includes one pizza roll and one bottled drink of choice. Taxes extra.</p>
  </main>
</body>
</html>
```